BSC Flyer to attract applicants 11x17

Brightline Stagecraft Company provides crew for local concerts, filming, theater, and corporate events.
The flyer will be posted on bulletin boards at colleges with theater programs.
Our primary venues are historic theaters in downtown LA
Need a 11x17 poster to attract potential applicants/crew
I have attached a poster that one of our staff made that has all if the relevant info - but i know the poster can look much better than that. I have also attached many images and our logo. It is not necessary to use all of the images, or any of them. The two images of the theater interiors are the venues we operate so they would be the first to include. I can send additional info or images upon request. Thank you

Entertainment

• APPLY@BSCCREWHUB.LA

```html
<!DOCTYPE html>
<html lang="en">
<head>
<meta charset="UTF-8">
<title>Brightline Stagecraft Company – Open Positions</title>
<link href="https://fonts.googleapis.com/css2?family=Cinzel:wght@700&family=Montserrat:wght@300;400;700;800;900&display=swap" rel="stylesheet">
<style>
  :root {
    --page-bg: #e4e7ec;
    --brand-blue: #1f5aab;
    --brand-blue-deep: #174a91;
    --navy: #0d1f45;
    --white: #ffffff;
    --accent-orange: #f2a23a;
    --accent-red: #b83a5a;
    --email-blue: #1f4fa8;
    --silver-top: #ffffff;
    --silver-bottom: #b9bcc4;
  }
  * { margin: 0; padding: 0; box-sizing: border-box; }
  html, body {
    width: 1200px; height: 900px; overflow: hidden;
    background: var(--page-bg);
  }
  .canvas { position: relative; width: 1200px; height: 900px; }
  .poster {
    position: absolute; left: 322px; top: 20px;
    width: 556px; height: 860px;
    overflow: hidden; background: var(--brand-blue);
  }
  .poster-shapes { position: absolute; inset: 0; }
  .logo-badge {
    position: absolute; left: 21px; top: 23px;
    width: 154px; height: 154px; border-radius: 50%;
    background: var(--white);
    border: 10px solid var(--brand-blue-deep);
    display: flex; align-items: center; justify-content: center;
    font-family: "Montserrat", sans-serif; font-weight: 800;
    font-size: 40px; color: var(--brand-blue);
  }
  .company-name {
    position: absolute; left: 35px; top: 382px; width: 324px;
    color: var(--white); font-family: "Cinzel", serif; font-weight: 700;
  }
  .company-name__main { font-size: 24px; line-height: 1; letter-spacing: -0.3px; white-space: nowrap; }
  .company-name__sub {
    display: flex; align-items: center; gap: 8px; margin-top: 6px;
    font-size: 17px; letter-spacing: 9px; line-height: 1;
  }
  .company-name__sub::before, .company-name__sub::after {
    content: ""; flex: 1; height: 2px; background: var(--white);
  }
  .company-name__sub span { margin-right: -9px; }
  .headline {
    position: absolute; left: 33px; top: 446px;
    font-family: "Montserrat", sans-serif; font-weight: 900;
    line-height: 1; text-transform: uppercase; white-space: nowrap;
    background: linear-gradient(180deg, var(--silver-top) 20%, var(--silver-bottom) 100%);
    -webkit-background-clip: text; background-clip: text; color: transparent;
    filter: drop-shadow(3px 4px 3px rgba(0,0,0,0.45));
  }
  .headline__line1 { font-size: 59px; letter-spacing: -1px; }
  .headline__line2 { font-size: 74px; letter-spacing: -1px; margin-top: -2px; }
  .intro {
    position: absolute; left: 35px; top: 594px; width: 515px;
    color: var(--white); font-family: "Montserrat", sans-serif; font-weight: 700;
    font-size: 25.5px; line-height: 32px; white-space: nowrap;
  }
  .accent-stripe {
    position: absolute; left: 0; top: 750px; width: 556px; height: 9px;
    background: linear-gradient(90deg, var(--accent-orange) 0%, var(--accent-orange) 45%, var(--accent-red) 60%, var(--accent-red) 100%);
  }
  .city-photo {
    position: absolute; left: 0; top: 759px; width: 556px; height: 101px;
    background: linear-gradient(180deg, #132d66 0%, #1a3c7c 45%, #0b1a3c 100%);
  }
  .apply-box {
    position: absolute; left: 124px; top: 710px; width: 300px; height: 88px;
    background: var(--white); border-radius: 14px;
    text-align: center; font-family: "Montserrat", sans-serif; color: var(--email-blue);
  }
  .apply-box__label { font-weight: 400; font-size: 15.5px; margin-top: 15px; }
  .apply-box__email { font-weight: 800; font-size: 19.5px; margin-top: 5px; letter-spacing: 0.2px; }
  .website {
    position: absolute; left: 0; top: 822px; width: 556px; text-align: center;
    color: var(--white); font-family: "Montserrat", sans-serif; font-weight: 800;
    font-size: 15px; letter-spacing: 5px;
  }
</style>
</head>
<body>
<div class="canvas">
  <div class="poster">
    <svg class="poster-shapes" width="556" height="860" viewBox="0 0 556 860">
      <defs>
        <linearGradient id="venueMainTones" x1="0" y1="0" x2="1" y2="1">
          <stop offset="0" stop-color="#3a1f5c"/>
          <stop offset="0.45" stop-color="#8a4a3a"/>
          <stop offset="0.7" stop-color="#5a2f6e"/>
          <stop offset="1" stop-color="#2a1838"/>
        </linearGradient>
        <linearGradient id="venueSecondTones" x1="0" y1="0" x2="1" y2="0">
          <stop offset="0" stop-color="#6b3b1e"/>
          <stop offset="0.6" stop-color="#c88a3c"/>
          <stop offset="1" stop-color="#9a2a24"/>
        </linearGradient>
        <linearGradient id="cornerBlue" x1="0" y1="0" x2="1" y2="1">
          <stop offset="0" stop-color="#2160b4"/>
          <stop offset="1" stop-color="#163f7d"/>
        </linearGradient>
      </defs>
      <rect x="0" y="0" width="556" height="460" fill="url(#venueMainTones)" role="img" aria-label="Photo of an ornate historic downtown LA theater interior with domed ceiling and stage"/>
      <polygon points="275,0 556,0 556,125" fill="url(#cornerBlue)"/>
      <polygon points="279,342 556,239 556,462" fill="url(#venueSecondTones)" role="img" aria-label="Photo of a gilded historic theater auditorium with red stage curtain"/>
      <line x1="262" y1="349" x2="556" y2="239" stroke="#f2a23a" stroke-width="3"/>
      <polygon points="0,373 154,288 556,462 556,860 0,860" fill="var(--brand-blue)"/>
    </svg>

    <div class="logo-badge">BSC</div>

    <div class="company-name">
      <div class="company-name__main">BRIGHTLINE STAGECRAFT</div>
      <div class="company-name__sub"><span>COMPANY</span></div>
    </div>

    <div class="headline">
      <div class="headline__line1">Has Open</div>
      <div class="headline__line2">Positions</div>
    </div>

    <p class="intro">We Are Looking For Talented<br>Technicians To Add To Our Roster<br>Of Skilled Professionals</p>

    <div class="accent-stripe"></div>
    <div class="city-photo" role="img" aria-label="Photo of the downtown Los Angeles skyline at night"></div>

    <div class="apply-box">
      <div class="apply-box__label">Send Resume To :</div>
      <div class="apply-box__email">APPLY@BSCCREWHUB.LA</div>
    </div>

    <div class="website">WWW.BSCCREWHUB.LA</div>
  </div>
</div>
</body>
</html>
```